Home Inspector

i do home inspections in Houston Texas. Would like a nice logo(maybe forest green and black). I inspect:foundations,structural,electric,plumbing,appliances,pools/spas and other optional systems.Hours mon-sat.

Contact Information for Business Card

BRIGHTWELL PROPERTY INSPECTIONS,5837 Tallow Creek,Houston,Texas,77268,Daniel Okafor,Professional Inspector,License#48726,Serving the Greater Houston Area

```html
<!DOCTYPE html>
<html lang="en">
<head>
<meta charset="utf-8">
<title>Brightwell Property Inspections – Business Card</title>
<link href="https://fonts.googleapis.com/css2?family=Lato:wght@400;700;900&display=swap" rel="stylesheet">
<style>
  :root {
    --stage: #5b5b5b;
    --paper: #ffffff;
    --ink: #1b1b1b;
    --night: #050505;
    --forest: #1e4d2b;
    --lime: #8dc63f;
    --light: #ffffff;
  }
  * { margin: 0; padding: 0; box-sizing: border-box; }
  html, body {
    width: 1200px;
    height: 900px;
    overflow: hidden;
    background: var(--stage);
    font-family: "Lato", Arial, sans-serif;
  }
  .business-card {
    position: absolute;
    left: 75px;
    top: 150px;
    width: 1050px;
    height: 600px;
    background: var(--paper);
    overflow: hidden;
  }
  .card-shapes {
    position: absolute;
    inset: 0;
    width: 1050px;
    height: 600px;
  }
  .swoosh-accent { fill: var(--forest); }
  .swoosh-dark { fill: var(--night); }
  .service-band { fill: var(--forest); }

  .brand {
    position: absolute;
    left: 130px;
    top: 110px;
    display: flex;
    align-items: center;
    gap: 34px;
  }
  .brand-dot {
    width: 96px;
    height: 96px;
    border-radius: 50%;
    background: var(--forest);
  }
  .brand-name {
    color: var(--ink);
    font-weight: 700;
    font-size: 38px;
    line-height: 1.12;
  }

  .inspector {
    position: absolute;
    left: 62px;
    top: 378px;
    color: var(--lime);
  }
  .inspector-name {
    font-size: 46px;
    font-weight: 400;
    line-height: 1.05;
  }
  .inspector-name strong { font-weight: 700; }
  .inspector-title {
    font-size: 22px;
    letter-spacing: 1.5px;
    text-transform: uppercase;
    margin-top: 4px;
  }

  .office {
    position: absolute;
    right: 62px;
    top: 272px;
    text-align: right;
    color: var(--light);
    font-size: 21px;
    line-height: 1.55;
    text-transform: uppercase;
  }
  .office-license {
    color: var(--lime);
    font-weight: 700;
    font-size: 24px;
    text-transform: none;
    margin-bottom: 2px;
  }

  .service-area {
    position: absolute;
    left: 0;
    top: 498px;
    width: 1050px;
    height: 102px;
    display: flex;
    align-items: center;
    justify-content: center;
    color: var(--light);
    font-size: 31px;
    font-weight: 700;
    letter-spacing: 6px;
    text-transform: uppercase;
  }
</style>
</head>
<body>
  <article class="business-card">
    <svg class="card-shapes" viewBox="0 0 1050 600" aria-hidden="true">
      <path class="swoosh-accent" d="M0,364 C350,320 760,262 1050,166 L1050,600 L0,600 Z"/>
      <path class="swoosh-dark" d="M0,376 C350,342 760,292 1050,208 L1050,600 L0,600 Z"/>
      <rect class="service-band" x="0" y="498" width="1050" height="102"/>
    </svg>

    <header class="brand">
      <span class="brand-dot"></span>
      <div class="brand-name">Brightwell<br>Property<br>Inspections</div>
    </header>

    <section class="inspector">
      <div class="inspector-name">Daniel <strong>Okafor</strong></div>
      <div class="inspector-title">Professional Inspector</div>
    </section>

    <address class="office" style="font-style:normal">
      <div class="office-license">License#48726</div>
      <div>5837 Tallow Creek,</div>
      <div>Houston, Texas,77268</div>
    </address>

    <footer class="service-area">Serving the Greater Houston Area</footer>
  </article>
</body>
</html>
```